Briefpapier klangrabatt17
Die Zusammenarbeit war vorbildlich. Sehr schnelle Reaktion auf unsere Wünsche und eine sehr gute Umsetzung des Projektes. Danke, wir werden wieder auf Sie zurückkommen für unseren nächsten Flyer.
Zielgruppe
Wir verkaufen Musiknoten, Lehr-DVDs für Instrumente aus Klassik, Rock, Pop, Jazz etc.
Da wir in letzter Zeit mehr Musiknoten aus der Klassik haben, wäre es sinnvoll, den Briefbogen seriös zu gestalten.
Aufgabenstellung
Wir bitten um Gestaltung eines Briefbogens mit den folgenden Informationen:
Anschrift: klangrabatt17
www.klangrabatt17.example
Wir haben folgende Homepage:
http://laden.tonfinder.example/38527/Home.html
Der Zusatz lyra digital sollte allerdings nicht im Brieflogo erscheinen.
Also Logo nur mit "klangrabatt17" und dem Zusatz: Ihr Spezialist für Musiknoten und Lehr-DVD's
Bitte die in der angefügten Datei verwandten Farben verwenden (gelb und rot)

```html
<!DOCTYPE html>
<html lang="de">
<head>
<meta charset="utf-8">
<title>Briefpapier klangrabatt17</title>
<link href="https://fonts.googleapis.com/css2?family=Source+Sans+3:wght@400;700;900&display=swap" rel="stylesheet">
<style>
  :root {
    --backdrop: #f7f7f7;
    --paper: #ffffff;
    --olive: #c9c21f;
    --red: #c4262e;
    --beige: #e7e5c3;
    --grey-text: #7b7b7b;
    --contact-text: #a3a386;
    --rule: #8a8a8a;
    --shadow: rgba(0,0,0,0.45);
  }
  html, body {
    margin: 0; padding: 0;
    width: 1200px; height: 1000px;
    overflow: hidden;
    background: var(--backdrop);
    font-family: "Source Sans 3", sans-serif;
  }
  .canvas { position: relative; width: 1200px; height: 1000px; }

  .wordmark {
    position: absolute; color: var(--olive);
    font-weight: 900; letter-spacing: -0.5px; white-space: nowrap;
    display: flex; align-items: center; gap: 7px; line-height: 1;
  }
  .wordmark__dot { width: 12px; height: 12px; border-radius: 50%; background: var(--red); }

  /* Letterhead */
  .letterhead {
    position: absolute; left: 29px; top: 111px; width: 533px; height: 754px;
    background: var(--paper);
    box-shadow: 4px 4px 6px var(--shadow);
    overflow: hidden;
  }
  .letterhead__side-band {
    position: absolute; right: 0; top: 0; width: 13px; height: 288px;
    background: var(--beige);
  }
  .letterhead .wordmark { right: 24px; top: 32px; font-size: 36px; }
  .sender-line {
    position: absolute; left: 121px; top: 146px;
    font-size: 8px; color: var(--grey-text);
    display: flex; align-items: center; gap: 3px;
  }
  .sender-line__dot { width: 4px; height: 4px; border-radius: 50%; background: var(--red); }
  .fold-mark { position: absolute; left: 0; width: 21px; height: 1px; background: var(--rule); }
  .fold-mark--upper { top: 263px; }
  .fold-mark--lower { top: 501px; }

  .footer-legal {
    position: absolute; left: 15px; top: 675px;
    font-size: 7.2px; line-height: 8.5px; color: var(--grey-text);
  }
  .footer-legal p { margin: 0 0 3px; }
  .footer-contact {
    position: absolute; right: 21px; top: 677px;
    font-size: 7.2px; line-height: 8.5px; color: var(--contact-text); text-align: right;
  }
  .footer-contact p { margin: 0 0 3px; }
  .label { color: var(--red); }
  .footer-contact .addr-block { display: inline-block; text-align: left; }
  .footer-contact .name { color: var(--red); display: block; }
  .footer-contact .addr { display: block; }

  .footer-band {
    position: absolute; left: 0; bottom: 0; width: 100%; height: 11px;
    background: var(--beige);
  }
  .web-tab {
    position: absolute; left: 179px; bottom: 0; width: 174px; height: 22px;
    background: var(--red);
    border-radius: 87px 87px 0 0 / 22px 22px 0 0;
    box-shadow: 0 0 0 3px var(--paper);
    color: #fff; font-size: 10px;
    display: flex; align-items: center; justify-content: center;
    padding-top: 2px; box-sizing: border-box;
  }

  /* Envelopes */
  .envelope { position: absolute; }
  .envelope--front { left: 600px; top: 133px; width: 560px; height: 384px; }
  .envelope--back { left: 600px; top: 538px; width: 561px; height: 291px; }
  .envelope__body {
    position: absolute; background: var(--paper);
    box-shadow: 2px 2px 4px var(--shadow);
    overflow: hidden;
  }
  .envelope--front .envelope__body {
    left: 0; top: 98px; width: 560px; height: 286px;
    border-top: 1px solid var(--rule); box-sizing: border-box;
  }
  .envelope--back .envelope__body { left: 0; top: 0; width: 561px; height: 291px; }
  .envelope__flap { position: absolute; left: 0; top: 0; }
  .envelope__sender {
    position: absolute; left: 43px; top: 39px;
    font-size: 8px; line-height: 10px; color: var(--grey-text);
  }
  .envelope__sender .name { color: var(--red); }
  .envelope__window {
    position: absolute; left: 39px; top: 154px; width: 222px; height: 88px;
    border-radius: 12px; box-sizing: border-box;
    border-top: 1.5px solid #9a9a9a; border-left: 1.5px solid #9a9a9a;
    border-right: 1px solid #eee; border-bottom: 1px solid #eee;
  }
  .envelope--front .wordmark { right: 33px; top: 197px; font-size: 34px; }
</style>
</head>
<body>
<div class="canvas">

  <section class="letterhead">
    <div class="letterhead__side-band"></div>
    <div class="wordmark">klangrabatt17<span class="wordmark__dot"></span></div>
    <div class="sender-line">Ahornweg 8<span class="sender-line__dot"></span>85099 Buchfeld</div>
    <div class="fold-mark fold-mark--upper"></div>
    <div class="fold-mark fold-mark--lower"></div>

    <div class="footer-legal">
      <p>Bankverbindung:<br>Lorenz Albrecht Kreissparkasse Buchfeld<br>BIC:&nbsp;&nbsp;&nbsp;BKBFDE21XXX<br>IBAN: DE00 1234 0000 0000 5678 90</p>
      <p>Geschäftsführer: Lorenz Albrecht<br>Steuernummer: 100-200-30040<br>UST-ID-Nr. DE 000111222</p>
    </div>

    <div class="footer-contact">
      <p><span class="addr-block"><span class="name">Lorenz Albrecht</span><span class="addr">Ahornweg 8</span><span class="addr">85099 Buchfeld</span></span></p>
      <p><span class="label">Tel.</span> 08400-1234<br><span class="label">Fax.</span> 08400-12345</p>
      <p><span class="label">E-mail.</span> info@klangrabatt17.example<br><span class="label">Web.</span> www.klangrabatt17.example</p>
    </div>

    <div class="footer-band"></div>
    <div class="web-tab">www.klangrabatt17.example</div>
  </section>

  <section class="envelope envelope--front">
    <svg class="envelope__flap" width="560" height="99" viewBox="0 0 560 99">
      <path d="M0 99 L0 80 Q0 56 32 48 L270 1 Q280 -1 290 1 L528 48 Q560 56 560 80 L560 99 Z" fill="var(--beige)"/>
    </svg>
    <div class="envelope__body">
      <div class="envelope__sender"><span class="name">Lorenz Albrecht</span><br>Ahornweg 8<br>85099 Buchfeld</div>
      <div class="envelope__window"></div>
      <div class="wordmark">klangrabatt17<span class="wordmark__dot"></span></div>
    </div>
  </section>

  <section class="envelope envelope--back">
    <div class="envelope__body"></div>
    <svg class="envelope__flap" width="561" height="100" viewBox="0 0 561 100">
      <path d="M0 0 L561 0 L561 20 Q561 44 528 51 L290 97 Q280 99 270 97 L32 51 Q0 44 0 20 Z" fill="var(--beige)"/>
    </svg>
  </section>

</div>
</body>
</html>
```